We require a business card that promotes our Electrical business. Things we would like included are;
1) our business name, Bright Path Electrical and Communication
2) Our Electrical licence, EC 73620
3) Our ABN, 41 297 506 183
4) Our website, www.korvanelectric.com.au
5) Our Email, info@korvanelectric.com.au
6) Our contact number, 0462 158 704
7) Our address, 57 Larkfield Rd West Dunmore Perth 6109
8) Our logo, I will attach this (can you please change it so the ackground is white not black)
9) Our colours are red and white and perhaps some black
10) Managing Director Tomasz Relhuvan
11) the back to say 'notes' and have some lines for writing

Target Market(s)

General

Industry/Entity Type

Electrical

Contact Information for Business Card

Include the colour white, black and red.

Font styles to use
Sans Serif

Requirements
Nice to have
• A thunder bolt or a power point or a cord or something electrical, cartoon image of a cartoon like electrical tradie

```html
<!DOCTYPE html>
<html lang="en">
<head>
<meta charset="utf-8">
<title>Bright Path Electrical &amp; Communication – Business Card</title>
<link rel="stylesheet" href="https://fonts.googleapis.com/css2?family=Lato:wght@300;400;700;900&display=swap">
<style>
  :root {
    --stage: #1c1c1c;
    --card: #262626;
    --card-light: #2f2f2f;
    --red: #d0202a;
    --white: #f2f2f2;
    --grey: #a9a9a9;
    --strip: #bdbdbd;
    --dots: #8a8a8a;
  }
  * { box-sizing: border-box; margin: 0; padding: 0; }
  html, body { width: 1200px; height: 873px; overflow: hidden; }
  body {
    background: var(--stage);
    font-family: "Lato", sans-serif;
    position: relative;
  }
  .card {
    position: absolute;
    width: 540px;
    height: 309px;
    top: 282px;
    border-radius: 3px;
    overflow: hidden;
    box-shadow: 0 10px 30px rgba(0,0,0,.55);
  }
  .card__texture {
    position: absolute; inset: 0;
    background: linear-gradient(135deg, var(--card-light) 0%, var(--card) 55%, #222 100%);
  }

  /* Back */
  .card--back { left: 40px; }
  .notes__title {
    position: absolute; left: 52px; top: 40px;
    color: var(--white); font-weight: 900; font-size: 38px; line-height: 1.05;
  }
  .notes__lines {
    position: absolute; left: 52px; right: 40px; top: 112px;
    display: flex; flex-direction: column; gap: 34px;
  }
  .notes__lines span { display: block; border-top: 2px dotted var(--dots); }

  /* Front */
  .card--front { left: 620px; }
  .business {
    position: absolute; left: 28px; top: 60px;
    color: var(--red); font-weight: 900; line-height: 1.1;
  }
  .business__name { font-size: 21px; text-align: center; width: 300px; }
  .business__trade { font-size: 21px; }
  .services {
    display: flex; margin-top: 6px;
    color: var(--white); font-size: 12.5px; font-weight: 700;
  }
  .services li { list-style: none; padding: 0 6px; border-left: 2px solid var(--red); }
  .services li:first-child { padding-left: 0; border-left: 0; }

  .brand-mark {
    position: absolute; right: 44px; top: 50px;
    display: flex; align-items: center; gap: 10px;
    color: var(--red); font-weight: 900; font-size: 20px;
  }
  .brand-mark__dot { width: 18px; height: 18px; border-radius: 50%; background: var(--red); }

  .director {
    position: absolute; right: 30px; top: 150px; text-align: right; line-height: 1.3;
  }
  .director__name { color: var(--red); font-weight: 900; font-size: 17px; }
  .director__role { color: var(--white); font-weight: 400; font-size: 12px; letter-spacing: .3px; }
  .director__licence { color: var(--red); font-weight: 700; font-size: 15px; }

  .contacts {
    position: absolute; left: 28px; top: 148px;
    list-style: none; display: flex; flex-direction: column; gap: 6px;
  }
  .contacts li {
    display: flex; align-items: center; gap: 10px;
    color: var(--red); font-weight: 700; font-size: 13px; line-height: 16px;
  }
  .contacts svg { width: 14px; height: 14px; flex: none; fill: none; stroke: var(--white); stroke-width: 1.6; }
  .contacts .icon-pin { fill: var(--white); stroke: none; }

  .card__bands { position: absolute; left: 0; bottom: 0; width: 540px; height: 30px; }
</style>
</head>
<body>

  <section class="card card--back" aria-label="Card back">
    <div class="card__texture" role="img" aria-label="Dark faceted background texture"></div>
    <p class="notes__title">Notes</p>
    <div class="notes__lines" aria-hidden="true">
      <span></span><span></span><span></span><span></span><span></span>
    </div>
  </section>

  <section class="card card--front" aria-label="Card front">
    <div class="card__texture" role="img" aria-label="Dark faceted background texture"></div>

    <div class="brand-mark">
      <span class="brand-mark__dot"></span>
      <span>Bright Path</span>
    </div>

    <div class="business">
      <p class="business__name">Bright Path</p>
      <p class="business__trade">Electrical &amp; Communication</p>
      <ul class="services">
        <li>Electrical</li>
        <li>Communication</li>
        <li>Air Conditioning</li>
      </ul>
    </div>

    <div class="director">
      <p class="director__name">Tomasz Relhuvan</p>
      <p class="director__role">MANAGING DIRECTOR</p>
      <p class="director__licence">EC 73620</p>
    </div>

    <ul class="contacts">
      <li>
        <svg viewBox="0 0 14 14"><rect x="3.5" y="1" width="7" height="12" rx="1.2"/><line x1="6" y1="11" x2="8" y2="11"/></svg>
        0462 158 704
      </li>
      <li>
        <svg viewBox="0 0 14 14"><rect x="1" y="3" width="12" height="8" rx="0.8"/><polyline points="1,3 7,8 13,3"/></svg>
        info@korvanelectric.com.au
      </li>
      <li>
        <svg viewBox="0 0 14 14"><circle cx="7" cy="7" r="5.5"/><line x1="1.5" y1="7" x2="12.5" y2="7"/><ellipse cx="7" cy="7" rx="2.4" ry="5.5"/></svg>
        www.korvanelectric.com.au
      </li>
      <li>
        <svg viewBox="0 0 14 14"><path class="icon-pin" d="M7 1a4 4 0 0 0-4 4c0 3 4 8 4 8s4-5 4-8a4 4 0 0 0-4-4zm0 5.5a1.5 1.5 0 1 1 0-3 1.5 1.5 0 0 1 0 3z"/></svg>
        57 Larkfield Rd West Dunmore Perth 6109
      </li>
      <li>
        <svg viewBox="0 0 14 14"><rect x="2" y="1" width="10" height="12" rx="1"/><line x1="4.5" y1="5" x2="9.5" y2="5"/><line x1="4.5" y1="8" x2="9.5" y2="8"/></svg>
        ABN 41 297 506 183
      </li>
    </ul>

    <svg class="card__bands" viewBox="0 0 540 30" aria-hidden="true">
      <rect x="0" y="20" width="540" height="10" fill="var(--strip)"/>
      <path d="M360 30 V18 Q360 6 376 6 H540 V30 Z" fill="var(--red)"/>
    </svg>
  </section>

</body>
</html>
```